New look and feel for investment website

Hi

Our website needs a crisp and professional look and feel applying to it. Here’s the address: http://www.brightplinth.co.uk. Since posting the brief yesterday (Tuesday, 16 August), we've reduced the amount of content on the home page, which should make life a little easier for you. We will come back later today, with some points of reference in terms of sites we like the look of. (See below)

17 August, 1.20pm GMT. OK, comments generally on the designs submitted so far. Please keep in mind that images of graphs, piles of coins, paper money and pretty females are not what is required. Better to think in terms of abstract imagery instead. Ratios? Circles? Relationships? Patterns? Not money,sex,graphs etc. Hope that helps.

For guidance on look and feel, please refer to these sites, which we like:

http://www.morvelle.co.uk/
http://www.qz.com/
https://www.harrowfieldtamsin.com
https://www.pirelconcerns.com
https://www.kvantule.com
Updates

Here's the Tall Beacons logo created in AI CS5.

Our market is professional financial advisers and relatively sophisticated private investors. The look and feel therefore should be slick and sophisticated - not 'lively' and lightweight, more like a banking site. Please read the brief again where we've added a list of websites that we really like the look of to get a better feel for what we're looking for. Thanks once again, we appreciate the work you're putting in.

It's essential that all the elements that are on the current home page be included on all new designs. 

We use a device in our e-mails which you may wish to incorporate in your design.

Target Market(s)

Professional financial advisers. People who know about investment and money.

Industry/Entity Type

Investment

Requirements
Should not have
• Graphs or people.

```html
<!DOCTYPE html>
<html lang="en">
<head>
<meta charset="utf-8">
<title>Tall Beacons – Home</title>
<link href="https://fonts.googleapis.com/css2?family=Arimo:wght@400;700&display=swap" rel="stylesheet">
<style>
:root{
  --orange:#f07d1c;
  --orange-dark:#d9660a;
  --ink:#333;
  --muted:#666;
  --grey:#bfbfbf;
  --grey-dark:#9a9a9a;
  --line:#d8d8d8;
  --hero:#e9e9e9;
  --red:#c8302a;
  --footer:#2f3a44;
}
*{box-sizing:border-box;margin:0;padding:0}
html,body{width:887px;height:1200px;overflow:hidden;background:#fff;font-family:"Arimo",Arial,sans-serif;color:var(--ink)}
.page{position:relative;width:887px;height:1200px}
.account{position:absolute;right:18px;top:10px;display:flex;gap:4px}
.account span{background:var(--grey-dark);color:#fff;font-size:10px;padding:3px 8px}
.brand{position:absolute;left:22px;top:30px;display:flex;align-items:center;gap:8px;font-size:34px;font-weight:700;color:#555;letter-spacing:-.5px}
.brand i{display:block;width:16px;height:16px;background:var(--orange)}
.nav{position:absolute;left:470px;top:48px;display:flex;gap:4px}
.nav a{background:var(--grey);color:#fff;font-size:12px;text-decoration:none;padding:10px 14px;width:96px;text-align:center}
.nav a.current{background:var(--orange)}
.hero{position:absolute;left:15px;top:86px;width:857px;height:252px;background:linear-gradient(90deg,#f4f4f4,var(--hero) 50%,#fafafa)}
.hero-art{position:absolute;left:0;top:0;width:100%;height:100%}
.hero h1{position:absolute;left:500px;top:138px;width:340px;font-size:20px;line-height:1.3;color:var(--orange);font-weight:400}
.side{position:absolute;left:15px;top:368px;width:220px}
.side ul{list-style:none;border-top:1px solid var(--line)}
.side li{font-size:11px;color:var(--muted);padding:8px 0 8px 14px;border-bottom:1px solid var(--line);position:relative}
.side li::before{content:"";position:absolute;left:2px;top:12px;width:5px;height:5px;background:var(--orange)}
.trial{margin-top:14px;background:var(--orange);color:#fff;padding:14px 14px 16px}
.trial h2{font-size:22px;margin-bottom:8px}
.trial p{font-size:10.5px;line-height:1.4}
.trial u{font-weight:700}
.main{position:absolute;left:250px;top:368px;width:622px}
.main h3{font-size:13px;color:var(--ink);margin:6px 0 5px}
.main p{font-size:10.5px;line-height:1.45;color:var(--muted);margin-bottom:7px}
.main p b{color:var(--ink)}
.stats{position:absolute;left:15px;top:792px;width:857px;display:grid;grid-template-columns:repeat(4,1fr);gap:14px 14px}
.stat{border:1px solid var(--line);height:92px;padding:10px 10px 6px;text-align:center;display:flex;flex-direction:column;justify-content:space-between}
.stat p{font-size:11px;font-weight:700;line-height:1.3}
.stat strong{font-size:24px;color:var(--orange)}
.disclaimer{position:absolute;left:15px;top:1005px;width:857px;font-size:9.5px;line-height:1.45;color:var(--muted)}
.footer{position:absolute;left:15px;top:1110px;width:857px;height:28px;background:var(--footer);color:#ddd;font-size:10.5px;display:flex;align-items:center;justify-content:space-between;padding:0 14px}
.footer nav{display:flex;gap:16px}
</style>
</head>
<body>
<div class="page">
  <div class="account"><span>Login</span><span>Register for FREE</span></div>
  <div class="brand"><i></i>Tall Beacons</div>
  <nav class="nav">
    <a class="current" href="#">Home</a><a href="#">Our recent goals</a><a href="#">Watch list</a><a href="#">FAQs</a>
  </nav>

  <section class="hero">
    <svg class="hero-art" viewBox="0 0 857 252" role="img" aria-label="Abstract artwork of overlapping circles suggesting ratios and relationships">
      <circle cx="250" cy="120" r="150" fill="#dcdcdc" opacity=".6"/>
      <circle cx="420" cy="90" r="110" fill="#d2d2d2" opacity=".5"/>
      <circle cx="330" cy="130" r="60" fill="var(--red)" opacity=".85"/>
      <circle cx="430" cy="160" r="28" fill="var(--red)" opacity=".7"/>
    </svg>
    <h1>A potential return of 23.57% a year from America's biggest businesses with the emphasis firmly on capital preservation.</h1>
  </section>

  <aside class="side">
    <ul>
      <li>Current &amp; year to date performance</li>
      <li>Other key numbers</li>
      <li>Back tested results</li>
      <li>History of all trades</li>
      <li>About our analysis</li>
      <li>About value investing</li>
      <li>The Halden 1000 and the Crestline 500 index</li>
    </ul>
    <div class="trial">
      <h2>Free trial period</h2>
      <p>If you would like to receive this portfolio's performance for six months <u>free of charge</u>, then please complete the <u>registration form</u>.</p>
    </div>
  </aside>

  <main class="main">
    <h3>Something different...</h3>
    <p>You may well be thinking that Tall Beacons is just another one of those share tipping services that promise the world. We are not. Our recommendations come from a detailed, numbers-led analysis of every company in the index, and we only act when the figures give us a genuine margin of safety.</p>
    <p>Well, we have a pleasant surprise for you: you couldn't be further from the truth.</p>
    <h3>No! No! No!</h3>
    <p>There's no newsletter to read, books to study, trials to watch or traders' secrets to be revealed. You never trade on hunches or headlines. We simply publish what we buy, when we buy it and when we sell, so you can judge every decision for yourself. No sales pressure, no hidden fees, no guesswork.</p>
    <h3>Undervalued and overlooked</h3>
    <p>Our program finds stocks that appear to be undervalued, i.e. where the price of a company's share does not reflect the real worth of its business. We confine our search to the largest companies in the market, those that are widely researched, soundly financed and least likely to fail.</p>
    <h3>We don't get it right every time...</h3>
    <p>But we do win more often than we lose. Roughly three quarters of all our trades have closed at a profit, and the portfolio has never lost more than a few percent in any single year since we began.</p>
    <p>An average of five trades a year and never more than five holdings at any one time, combined with patience, is what keeps the risk low and the results steady. That's it. You don't have to do a thing more.</p>
    <p>For a concise explanation of our service and the results to date, <b>please get here</b>.</p>
  </main>

  <section class="stats">
    <div class="stat"><p>Average, annualised compound return over 5+ years</p><strong>23.57 %</strong></div>
    <div class="stat"><p>So far this year, the portfolio's return is</p><strong>13.49 %</strong></div>
    <div class="stat"><p>Worst ever annual loss: -3.49 %; best ever annual gain</p><strong>69.77 %</strong></div>
    <div class="stat"><p>Average return per trade including losing trades</p><strong>24.44 %</strong></div>
    <div class="stat"><p>Maximum number of winning/losing trades in a row</p><strong>11/4</strong></div>
    <div class="stat"><p>Average number of days a stock stays in the portfolio</p><strong>287</strong></div>
    <div class="stat"><p>An average of five trades a year and never more than five holdings at any one time</p><strong>5</strong></div>
    <div class="stat"><p>96 trades in total, of which 85 were profitable - a success rate of</p><strong>75.58 %</strong></div>
  </section>

  <p class="disclaimer">If you have any questions, please e-mail help@brightplinth.co.uk. Although we try to answer queries quickly, we are unable to give personal advice and nothing on this site should be taken as a recommendation to buy or sell any investment. The value of shares can fall as well as rise and past performance is no guide to future returns. This website is published by Tall Beacons Ltd, registered in England. All content is the copyright of Tall Beacons Ltd and may not be reproduced without our written permission. Please read our terms of service and privacy policy before registering.</p>

  <footer class="footer">
    <nav><span>Terms of Service</span><span>Privacy Policy</span></nav>
    <span>Tall Beacons 2011 © All rights reserved</span>
  </footer>
</div>
</body>
</html>
```